Wochen Speiseplan
Zielgruppe
Hospiz
Aufgabenstellung
Wir brauchen für unser Hospiz einen Wochenspeiseplan. Es soll eine Powerpointseite im A4 Format erstellt werden. Wir brauchen 4 unterschiedliche Seiten - für jede Jahreszeit einen Entwurf. Der Speiseplan soll von uns selbst ausgefüllt werden können.
Inhalte: Montag - Sonntag jeweils Mittag- und Abendessen. (Aufgebaut wie ein Stundenplan.). Möglichst große Schriftgröße. In der Fußnote bitte: "Änderungen vorbehalten schreiben". Das ganze soll professionell, aber dennoch liebevoll gestaltet sein. Es soll unseren Bewohnern "Liust machen" draufzuschauen. Der Plan wird jede Woche neu ausgefüllt, ausgedruckt und laminiert. Sollte also einfach zu handhaben sein.
Das Hospiz lebt von Spenden, daher bitte nicht zu aufwendig, dafür aber bezahlbar machen.

```html
<!DOCTYPE html>
<html lang="de">
<head>
<meta charset="utf-8">
<title>Wochenspeiseplan</title>
<link href="https://fonts.googleapis.com/css2?family=Sniglet:wght@400;800&family=Andika:ital,wght@0,400;0,700;1,700&family=Gelasio:ital@1&display=swap" rel="stylesheet">
<style>
  :root {
    --bg-yellow: #fdd25a;
    --bg-yellow-light: #fee08a;
    --banner-orange: #f39207;
    --banner-shadow: rgba(150, 80, 0, 0.35);
    --white: #ffffff;
    --day-orange: #e9880f;
    --row-lunch: #f9e88c;
    --row-dinner: #fde8d8;
    --text-dark: #2a2418;
  }
  * { margin: 0; padding: 0; box-sizing: border-box; }
  html, body { width: 1200px; height: 900px; overflow: hidden; }
  body { position: relative; font-family: "Andika", sans-serif; color: var(--text-dark); }

  .floral-backdrop {
    position: absolute; inset: 0;
    background:
      radial-gradient(circle at 12% 18%, var(--bg-yellow-light) 0, transparent 28%),
      radial-gradient(circle at 90% 85%, var(--bg-yellow-light) 0, transparent 30%),
      var(--bg-yellow);
  }

  .title-banner { position: absolute; top: 0; left: 0; width: 1200px; height: 300px; }

  .page-title {
    position: absolute; left: 298px; top: 50px;
    font-family: "Sniglet", sans-serif; font-weight: 400;
    font-size: 80px; color: var(--white); letter-spacing: 1px;
    transform: rotate(-1.5deg);
  }
  .page-subtitle {
    position: absolute; left: 450px; top: 178px;
    font-family: "Gelasio", serif; font-style: italic;
    font-size: 27px; color: var(--white);
    transform: rotate(-5deg); transform-origin: left center;
  }

  .menu-table {
    position: absolute; left: 37px; top: 328px; width: 1130px;
    border-collapse: collapse; table-layout: fixed;
  }
  .menu-table th, .menu-table td {
    border: 2px solid var(--white);
    text-align: left; vertical-align: top;
    padding: 8px 12px;
  }
  .menu-table th {
    background: var(--white); height: 52px;
    font-weight: 700; font-style: italic; font-size: 27px;
    color: var(--day-orange); padding-top: 6px;
  }
  .menu-table td { font-size: 22px; line-height: 1.27; padding-top: 10px; }
  .meal-lunch td { background: var(--row-lunch); height: 207px; }
  .meal-dinner td { background: var(--row-dinner); height: 208px; }

  .footnote {
    position: absolute; right: 42px; top: 806px;
    font-weight: 700; font-style: italic; font-size: 20px;
  }
</style>
</head>
<body>
  <div class="floral-backdrop" role="img" aria-label="Zartes Blumenmuster in hellem Gelb als Hintergrund"></div>

  <svg class="title-banner" viewBox="0 0 1200 300" aria-hidden="true">
    <path d="M258 0 H1200 V202 L300 285 Q276 287 274 262 Z" fill="var(--banner-shadow)" transform="translate(4 6)"/>
    <path d="M252 0 H1200 V200 L296 280 Q272 282 270 258 Z" fill="var(--banner-orange)"/>
  </svg>
  <h1 class="page-title">Wochenspeiseplan</h1>
  <p class="page-subtitle">Wir wünschen einen guten Appetit!</p>

  <table class="menu-table">
    <thead>
      <tr><th>Mo</th><th>Di</th><th>Mi</th><th>Do</th><th>Fr</th><th>Sa</th><th>So</th></tr>
    </thead>
    <tbody>
      <tr class="meal-lunch">
        <td>Spaghetti Bolognese</td>
        <td>Gemüse-<br>pfanne mit Hähnchen-<br>brust</td>
        <td>Milchreis mit<br>Zucker/<br>Zimt<br>und Kirsch-<br>kompott</td>
        <td>Nudelein-<br>topf mit Geflügel-<br>fleisch</td>
        <td>Germ-<br>knödel mit Pflaumen-<br>mus-<br>füllung</td>
        <td>3 gekochte Eier mit Senfsoße und<br>Kartoffeln</td>
        <td>Linsenein-<br>topf mit Bockwurst, Fladenbrot</td>
      </tr>
      <tr class="meal-dinner">
        <td>Chicken Wrap mit buntem Salat und Guacamole</td>
        <td>Gebratener Seehecht in Ei-Hülle dazu Kartoffel-<br>püree</td>
        <td>Frikadelle schwä-<br>bische Art auf Kräuter-<br>spätzle</td>
        <td>Gegrillte Schweins-<br>haxe</td>
        <td>Nudel-<br>Schinken-<br>Gratin<br>dazu gemischter Salat</td>
        <td>Kartoffel-<br>rösti mit Tomaten-<br>Schnitt-<br>lauch-<br>Quark</td>
        <td>Kochklopse Königs-<br>berger Art mit Kartoffeln/<br>Reis</td>
      </tr>
    </tbody>
  </table>

  <p class="footnote">Änderungen vorbehalten</p>
</body>
</html>
```